Adjust children's activity materials to branding and theme

Hello, we are a global kindergarten (nursery) chain and would like to provide branded printable activity sheets for our schools around the world, that would also reflect the theme of the curriculum.
We can provide the activity sheets that then need to be converted to our style and branded with our logo, colours and branding elements and include an item that reflects the theme, in our visual style. A full branding and colour codes guide is available for the chosen artist.

The 'grapheme' booklet attachment is provided as an example, please let us know how many similar pages you would be able to process within the budget. Each page is a standalone design task and can be printed out individually or as a booklet.

Industry/Entity Type

Early Education

Requirements
Must have
• BrightNest branding

```html
<!DOCTYPE html>
<html lang="en">
<head>
<meta charset="utf-8">
<title>BrightNest – Tracing Lines Worksheet, Page 2</title>
<link rel="stylesheet" href="https://fonts.googleapis.com/css2?family=Ubuntu:ital,wght@0,500;0,700;1,700&display=swap">
<style>
  :root {
    --brand-teal: #78abad;
    --ink: #000000;
    --guide: #9a9a9a;
    --paper: #ffffff;
    --picture-fill: #e6f0f0;
  }
  html, body {
    margin: 0;
    padding: 0;
    overflow: hidden;
    background: var(--paper);
  }
  .sheet {
    position: relative;
    width: 849px;
    height: 1200px;
    overflow: hidden;
    background: var(--paper);
    font-family: "Ubuntu", sans-serif;
  }
  .top-band {
    position: absolute;
    left: 0; top: 0;
    width: 849px; height: 19px;
    background: var(--brand-teal);
  }
  .exercises {
    position: absolute;
    left: 0; top: 0;
    width: 849px; height: 1200px;
  }
  .guide-line { stroke: var(--guide); stroke-width: 1.5; }
  .dot { fill: var(--paper); stroke: var(--ink); stroke-width: 2; }
  .capsule { fill: none; stroke: var(--ink); stroke-width: 2.2; }
  .solid { stroke: var(--ink); stroke-width: 5; fill: none; }
  .dash-long { stroke: var(--ink); stroke-width: 5; stroke-dasharray: 12 8; fill: none; }
  .dash-med { stroke: var(--ink); stroke-width: 5; stroke-dasharray: 8 14; fill: none; }
  .dash-sparse { stroke: var(--ink); stroke-width: 5; stroke-dasharray: 8 22; fill: none; }
  .dot-small { stroke: var(--ink); stroke-width: 4; stroke-dasharray: 5 9; fill: none; }
  .dot-sparse { stroke: var(--ink); stroke-width: 4; stroke-dasharray: 6 30; fill: none; }
  .dot-tight { stroke: var(--ink); stroke-width: 3; stroke-dasharray: 3 6; fill: none; }
  .trace-path { stroke: var(--ink); stroke-width: 4; stroke-dasharray: 12 8; fill: none; }
  .arrow { stroke: var(--ink); stroke-width: 2; fill: none; }
  .arrow-head { fill: var(--ink); }
  .picture-area { fill: var(--picture-fill); }
  .footer-bar {
    position: absolute;
    left: 1px; top: 1166px;
    width: 622px; height: 34px;
    background: var(--brand-teal);
  }
  .brand-name {
    position: absolute;
    left: 634px; top: 1166px;
    height: 34px;
    line-height: 34px;
    margin: 0;
    font-size: 21px;
    font-weight: 500;
    color: var(--brand-teal);
  }
  .page-tab {
    position: absolute;
    left: 753px; top: 1166px;
    width: 96px; height: 34px;
    background: var(--brand-teal);
    color: var(--paper);
    font-size: 14px;
    font-style: italic;
    font-weight: 700;
    line-height: 34px;
    text-align: center;
    padding-left: 8px;
    box-sizing: border-box;
  }
</style>
</head>
<body>
<main class="sheet">
  <div class="top-band"></div>

  <svg class="exercises" viewBox="0 0 1624 2296" xmlns="http://www.w3.org/2000/svg">
    <defs>
      <g id="arrow-down">
        <line class="arrow" x1="0" y1="0" x2="0" y2="68"/>
        <polygon class="arrow-head" points="-12,64 12,64 0,88"/>
      </g>
      <g id="arrow-right">
        <line class="arrow" x1="0" y1="0" x2="64" y2="0"/>
        <polygon class="arrow-head" points="62,-12 62,12 88,0"/>
      </g>
    </defs>

    <!-- Vertical strokes between two guide lines -->
    <g class="exercise vertical-strokes">
      <line class="guide-line" x1="5" y1="82" x2="1610" y2="82"/>
      <line class="guide-line" x1="5" y1="294" x2="1610" y2="294"/>
      <line class="solid" x1="57" y1="82" x2="57" y2="294"/>
      <line class="dash-long" x1="184" y1="94" x2="184" y2="282"/>
      <line class="dash-long" x1="315" y1="94" x2="315" y2="282"/>
      <line class="dash-long" x1="443" y1="94" x2="443" y2="282"/>
      <line class="dash-long" x1="580" y1="94" x2="580" y2="282"/>
      <line class="dash-med" x1="713" y1="108" x2="713" y2="272"/>
      <line class="dash-med" x1="844" y1="108" x2="844" y2="272"/>
      <line class="dash-sparse" x1="978" y1="115" x2="978" y2="160"/>
      <line class="dash-sparse" x1="1120" y1="115" x2="1120" y2="160"/>
      <use href="#arrow-down" x="161" y="90"/>
      <use href="#arrow-down" x="289" y="90"/>
      <use href="#arrow-down" x="420" y="90"/>
      <g>
        <circle class="dot" cx="184" cy="83" r="8"/><circle class="dot" cx="184" cy="295" r="8"/>
        <circle class="dot" cx="315" cy="83" r="8"/><circle class="dot" cx="315" cy="295" r="8"/>
        <circle class="dot" cx="443" cy="83" r="8"/><circle class="dot" cx="443" cy="295" r="8"/>
        <circle class="dot" cx="580" cy="83" r="8"/><circle class="dot" cx="580" cy="295" r="8"/>
        <circle class="dot" cx="713" cy="80" r="8"/><circle class="dot" cx="713" cy="293" r="8"/>
        <circle class="dot" cx="844" cy="80" r="8"/><circle class="dot" cx="844" cy="293" r="8"/>
        <circle class="dot" cx="978" cy="80" r="8"/><circle class="dot" cx="978" cy="293" r="8"/>
        <circle class="dot" cx="1120" cy="83" r="8"/><circle class="dot" cx="1120" cy="295" r="8"/>
        <circle class="dot" cx="1251" cy="83" r="8"/><circle class="dot" cx="1251" cy="295" r="8"/>
        <circle class="dot" cx="1382" cy="83" r="8"/><circle class="dot" cx="1382" cy="295" r="8"/>
        <circle class="dot" cx="1516" cy="83" r="8"/><circle class="dot" cx="1516" cy="295" r="8"/>
      </g>
    </g>

    <!-- Horizontal strokes on one guide line -->
    <g class="exercise horizontal-strokes">
      <line class="guide-line" x1="5" y1="515" x2="1610" y2="515"/>
      <line class="solid" x1="59" y1="515" x2="184" y2="515"/>
      <line class="dash-med" x1="325" y1="515" x2="433" y2="515" style="stroke-dasharray:8 24"/>
      <line class="dash-med" x1="590" y1="515" x2="703" y2="515" style="stroke-dasharray:8 24"/>
      <line class="dash-med" x1="886" y1="515" x2="946" y2="515" style="stroke-dasharray:8 36"/>
      <line class="dash-med" x1="1162" y1="515" x2="1222" y2="515" style="stroke-dasharray:8 36"/>
      <line class="dash-med" x1="1424" y1="515" x2="1484" y2="515" style="stroke-dasharray:8 36"/>
      <use href="#arrow-right" x="312" y="490"/>
      <g>
        <circle class="dot" cx="59" cy="516" r="8"/><circle class="dot" cx="184" cy="516" r="8"/>
        <circle class="dot" cx="315" cy="516" r="8"/><circle class="dot" cx="443" cy="516" r="8"/>
        <circle class="dot" cx="580" cy="516" r="8"/><circle class="dot" cx="713" cy="514" r="8"/>
        <circle class="dot" cx="844" cy="514" r="8"/><circle class="dot" cx="978" cy="514" r="8"/>
        <circle class="dot" cx="1120" cy="516" r="8"/><circle class="dot" cx="1251" cy="516" r="8"/>
        <circle class="dot" cx="1382" cy="516" r="8"/><circle class="dot" cx="1516" cy="516" r="8"/>
      </g>
    </g>

    <!-- Vertical strokes inside tracks -->
    <g class="exercise vertical-tracks">
      <rect class="capsule" x="53" y="685" width="44" height="208" rx="22"/>
      <rect class="capsule" x="176" y="685" width="44" height="208" rx="22"/>
      <rect class="capsule" x="299" y="685" width="44" height="208" rx="22"/>
      <rect class="capsule" x="422" y="685" width="44" height="208" rx="22"/>
      <rect class="capsule" x="544" y="685" width="44" height="208" rx="22"/>
      <rect class="capsule" x="667" y="685" width="44" height="208" rx="22"/>
      <rect class="capsule" x="789" y="685" width="44" height="208" rx="22"/>
      <rect class="capsule" x="912" y="685" width="44" height="208" rx="22"/>
      <rect class="capsule" x="1035" y="685" width="44" height="208" rx="22"/>
      <rect class="capsule" x="1158" y="685" width="44" height="208" rx="22"/>
      <rect class="capsule" x="1280" y="685" width="44" height="208" rx="22"/>
      <rect class="capsule" x="1403" y="685" width="44" height="208" rx="22"/>
      <rect class="capsule" x="1526" y="685" width="44" height="208" rx="22"/>
      <line class="solid" x1="75" y1="690" x2="75" y2="885"/>
      <line class="dash-long" x1="198" y1="700" x2="198" y2="878" style="stroke-width:4"/>
      <line class="dash-long" x1="321" y1="700" x2="321" y2="878" style="stroke-width:4"/>
      <line class="dash-long" x1="444" y1="700" x2="444" y2="878" style="stroke-width:4"/>
      <line class="dash-long" x1="566" y1="700" x2="566" y2="878" style="stroke-width:4"/>
      <line class="dot-sparse" x1="689" y1="716" x2="689" y2="870"/>
      <line class="dot-sparse" x1="811" y1="716" x2="811" y2="870"/>
      <line class="dot-tight" x1="934" y1="697" x2="934" y2="762"/>
      <line class="dot-small" x1="1057" y1="700" x2="1057" y2="756" style="stroke-dasharray:5 10"/>
      <use href="#arrow-down" x="156" y="684"/>
      <use href="#arrow-down" x="279" y="684"/>
      <use href="#arrow-down" x="404" y="684"/>
      <g>
        <circle class="dot" cx="75" cy="688" r="8"/><circle class="dot" cx="75" cy="887" r="8"/>
        <circle class="dot" cx="198" cy="688" r="8"/><circle class="dot" cx="198" cy="887" r="8"/>
        <circle class="dot" cx="321" cy="688" r="8"/><circle class="dot" cx="321" cy="887" r="8"/>
        <circle class="dot" cx="444" cy="688" r="8"/><circle class="dot" cx="444" cy="887" r="8"/>
        <circle class="dot" cx="566" cy="688" r="8"/><circle class="dot" cx="566" cy="887" r="8"/>
        <circle class="dot" cx="689" cy="688" r="8"/><circle class="dot" cx="689" cy="887" r="8"/>
        <circle class="dot" cx="811" cy="688" r="8"/><circle class="dot" cx="811" cy="887" r="8"/>
        <circle class="dot" cx="934" cy="688" r="8"/><circle class="dot" cx="934" cy="887" r="8"/>
        <circle class="dot" cx="1057" cy="688" r="8"/><circle class="dot" cx="1057" cy="887" r="8"/>
        <circle class="dot" cx="1180" cy="688" r="8"/><circle class="dot" cx="1180" cy="887" r="8"/>
        <circle class="dot" cx="1302" cy="688" r="8"/><circle class="dot" cx="1302" cy="887" r="8"/>
        <circle class="dot" cx="1425" cy="688" r="8"/><circle class="dot" cx="1425" cy="887" r="8"/>
        <circle class="dot" cx="1548" cy="688" r="8"/><circle class="dot" cx="1548" cy="887" r="8"/>
      </g>
    </g>

    <!-- Horizontal strokes inside tracks -->
    <g class="exercise horizontal-tracks">
      <rect class="capsule" x="53" y="1095" width="208" height="43" rx="21.5"/>
      <rect class="capsule" x="380" y="1095" width="205" height="43" rx="21.5"/>
      <rect class="capsule" x="710" y="1095" width="205" height="43" rx="21.5"/>
      <rect class="capsule" x="1038" y="1095" width="205" height="43" rx="21.5"/>
      <rect class="capsule" x="1368" y="1095" width="205" height="43" rx="21.5"/>
      <line class="solid" x1="58" y1="1116" x2="256" y2="1116"/>
      <line class="dash-long" x1="401" y1="1116" x2="568" y2="1116" style="stroke-width:4;stroke-dasharray:11 11"/>
      <line class="dash-long" x1="731" y1="1116" x2="898" y2="1116" style="stroke-width:4;stroke-dasharray:11 11"/>
      <use href="#arrow-right" x="380" y="1076"/>
      <use href="#arrow-right" x="705" y="1073"/>
      <g>
        <circle class="dot" cx="53" cy="1114" r="8"/><circle class="dot" cx="261" cy="1114" r="8"/>
        <circle class="dot" cx="380" cy="1114" r="8"/><circle class="dot" cx="585" cy="1114" r="8"/>
        <circle class="dot" cx="710" cy="1114" r="8"/><circle class="dot" cx="915" cy="1114" r="8"/>
        <circle class="dot" cx="1038" cy="1114" r="8"/><circle class="dot" cx="1243" cy="1114" r="8"/>
        <circle class="dot" cx="1368" cy="1114" r="8"/><circle class="dot" cx="1573" cy="1114" r="8"/>
      </g>
    </g>

    <!-- Square wave path -->
    <g class="exercise square-wave">
      <line class="guide-line" x1="8" y1="1355" x2="1614" y2="1355"/>
      <line class="guide-line" x1="8" y1="1568" x2="1614" y2="1568"/>
      <path class="trace-path" d="M75 1568 H140 V1357 H331 V1568 H521 V1355 H713"/>
      <g transform="translate(75 1548)">
        <line class="arrow" x1="0" y1="0" x2="40" y2="0"/>
        <polygon class="arrow-head" points="32,-12 32,12 58,0"/>
      </g>
      <g>
        <circle class="dot" cx="138" cy="1356" r="8"/><circle class="dot" cx="140" cy="1569" r="8"/>
        <circle class="dot" cx="329" cy="1356" r="8"/><circle class="dot" cx="331" cy="1569" r="8"/>
        <circle class="dot" cx="519" cy="1356" r="8"/><circle class="dot" cx="522" cy="1569" r="8"/>
        <circle class="dot" cx="713" cy="1354" r="8"/><circle class="dot" cx="716" cy="1569" r="8"/>
        <circle class="dot" cx="899" cy="1354" r="8"/><circle class="dot" cx="901" cy="1569" r="8"/>
        <circle class="dot" cx="1092" cy="1354" r="8"/><circle class="dot" cx="1095" cy="1569" r="8"/>
        <circle class="dot" cx="1283" cy="1354" r="8"/><circle class="dot" cx="1283" cy="1569" r="8"/>
        <circle class="dot" cx="1474" cy="1354" r="8"/><circle class="dot" cx="1477" cy="1569" r="8"/>
      </g>
    </g>

    <!-- Tracing pictures -->
    <rect class="picture-area" x="82" y="1705" width="510" height="475" rx="12"
          role="img" aria-label="Dotted outline of a blocky animal to trace"/>
    <rect class="picture-area" x="918" y="1672" width="629" height="515" rx="12"
          role="img" aria-label="Dotted outline of a blocky toy train to trace"/>
  </svg>

  <footer>
    <div class="footer-bar"></div>
    <p class="brand-name">BrightNest</p>
    <div class="page-tab">Page 2</div>
  </footer>
</main>
</body>
</html>
```